Design a website for a quickly growing ghostwriting and editing firm

NRF Productions has a website through Wix, but we need help! We are based in Austin, TX, and we work primarily with self-help, wellness, and diet authors. We offer ghostwriting, editing and book development services. You can see our basic site now at www.nadiafernproductions.com

```html
<!DOCTYPE html>
<html lang="en">
<head>
<meta charset="utf-8">
<title>NRF Productions</title>
<link rel="stylesheet" href="https://fonts.googleapis.com/css2?family=Righteous&family=Montserrat:wght@400;500;600&display=swap">
<style>
:root{
  --brown:#94490a;
  --brown-dark:#7e3d06;
  --brown-light:#b97a33;
  --orange:#e27b10;
  --ink:#2b2b2b;
  --cream:#efe6d6;
  --white:#ffffff;
  --display:'Righteous', sans-serif;
  --body:'Montserrat', sans-serif;
}
*{box-sizing:border-box;margin:0;padding:0}
html,body{width:1200px;height:3827px;overflow:hidden;background:var(--white)}
body{font-family:var(--body);color:var(--ink)}
.page{position:relative;width:1200px;height:3827px;overflow:hidden}
.abs{position:absolute}
.display{font-family:var(--display);text-transform:uppercase;font-weight:400}

.hero-photo{left:0;top:0;width:1200px;height:613px;background:linear-gradient(100deg,#f1eadc 0%,#ece2cf 55%,#d9c6a8 78%,#e8dcc6 100%)}
.brand{display:flex;align-items:center;gap:14px}
.brand-dot{width:66px;height:66px;border-radius:50%;background:var(--brown-light);flex:none}
.brand-name{font-family:var(--body);font-weight:500;color:var(--brown);font-size:26px;letter-spacing:.5px}
.nav{left:624px;top:46px;display:flex;gap:24px;font-family:var(--display);font-size:14px;text-transform:uppercase;color:var(--ink)}
.nav span:nth-child(5){margin-left:16px}
.hero-title{left:171px;top:172px;font-size:60px;line-height:74px;color:#2f2f2f}
.hero-text{left:171px;top:345px;width:600px;font-size:13.5px;line-height:25px;color:#2f2f2f}
.btn{display:flex;align-items:center;justify-content:center;border-radius:30px;background:linear-gradient(180deg,#a9641f,#8a4508);color:var(--white);font-family:var(--display);text-transform:uppercase}
.hero-btn{left:171px;top:420px;width:129px;height:57px;font-size:17px}

.austin{left:172px;top:558px;width:856px;height:266px}
.austin-title{left:0;top:40px;width:856px;text-align:center;font-size:38px;color:var(--white)}
.austin-sub{left:0;top:112px;width:856px;text-align:center;font-family:var(--display);font-size:21px;color:var(--white)}
.austin-badge{left:390px;top:181px;width:76px;height:76px;border-radius:50%;background:var(--white);border:5px solid #d9b88c}

.eyebrow{font-family:var(--display);text-transform:uppercase;color:var(--brown);font-size:17px}
.section-title{font-size:38px;color:var(--brown)}
.about-eyebrow{left:171px;top:920px}
.about-title{left:171px;top:943px}
.about-text{left:171px;top:1012px;width:440px;font-size:12.5px;line-height:22.5px;text-align:justify;color:#333}
.about-btn{left:174px;top:1192px;width:105px;height:45px;font-size:14px}
.about-ring{left:700px;top:928px;width:326px;height:326px;border-radius:50%;border-left:4px solid var(--brown)}
.about-photo{left:700px;top:928px;width:326px;height:326px;border-radius:50%;background:radial-gradient(circle at 55% 60%,#fbd98a 0%,#f1a447 45%,#c9782d 100%)}
.about-badge{left:683px;top:1129px;width:124px;height:124px;border-radius:50%;background:var(--white);border:6px solid #f3e9da;box-shadow:0 0 0 3px var(--brown-light) inset}

.work{left:0;top:1344px;width:1200px;height:713px}
.work-eyebrow{left:0;top:1487px;width:1200px;text-align:center;color:var(--white);font-size:15px}
.work-title{left:0;top:1510px;width:1200px;text-align:center;color:var(--white);font-size:38px}
.service{width:300px;text-align:center;color:var(--white)}
.service-icon{width:178px;height:178px;border-radius:50%;background:var(--white);border:6px solid #f3e2cc;margin:0 auto;display:flex;align-items:center;justify-content:center}
.service h3{font-family:var(--display);font-weight:400;text-transform:uppercase;font-size:28px;margin-top:34px}
.service p{font-size:12px;line-height:21px;margin-top:10px}

.offer-eyebrow{left:0;top:2110px;width:1200px;text-align:center}
.offer-title{left:0;top:2134px;width:1200px;text-align:center}
.card{top:2231px;width:266px;height:393px;border-radius:34px;overflow:hidden;background:var(--brown)}
.card-photo{position:absolute;left:0;top:0;width:266px;height:323px;border-radius:34px 34px 34px 34px/34px 34px 40px 40px}
.card-label{position:absolute;left:0;bottom:22px;width:266px;text-align:center;font-family:var(--display);text-transform:uppercase;color:var(--white);font-size:20px}

.subscribe{left:0;top:2718px;width:1200px;height:705px}
.sub-eyebrow{left:171px;top:2934px;color:var(--white);font-size:17px}
.sub-title{left:171px;top:2960px;color:var(--white);font-size:38px}
.sub-text{left:171px;top:3030px;width:480px;font-size:12.5px;line-height:23px;color:var(--white)}
.email{left:174px;top:3104px;width:408px;height:59px;border-radius:30px;background:var(--white);font-size:13px;padding-left:16px;display:flex;align-items:center;color:#222}
.sub-btn{left:175px;top:3182px;width:126px;height:60px;font-size:17px}

.footer-brand{left:172px;top:3544px;width:280px}
.footer-brand .brand-dot{width:78px;height:78px}
.footer-brand .brand-name{font-size:28px;line-height:32px;width:170px}
.col{font-size:12px;font-weight:500;text-transform:uppercase;color:#222}
.col h4{font-family:var(--display);font-weight:400;color:var(--brown-light);font-size:19px;margin-bottom:18px}
.col li{list-style:none;height:27.6px}
.map{left:781px;top:3465px;width:247px;height:231px;border-radius:30px;background:linear-gradient(135deg,#cfe3cf,#e6ece0 55%,#d5e4f0)}
.rule{left:172px;top:3750px;width:856px;height:1px;background:#555}
.copy{left:0;top:3777px;width:1200px;text-align:center;font-size:11px;color:#222}
</style>
</head>
<body>
<div class="page">

  <!-- Hero -->
  <div class="abs hero-photo" role="img" aria-label="Young girl in glasses reading a book while sitting on a stack of books against a white brick wall"></div>
  <div class="abs brand" style="left:171px;top:22px"><span class="brand-dot"></span><span class="brand-name">NRF Productions</span></div>
  <nav class="abs nav"><span>Home</span><span>About</span><span>Blog</span><span>Events</span><span>Authors</span><span>Contact</span></nav>
  <h1 class="abs display hero-title">NadiaFern<br>Productions</h1>
  <p class="abs hero-text">Sed ut perspiciatis unde omnis iste natus error sit voluptatem accusantium<br>dolor emque laudantium, totam rem aperiam.ipsam voluptatem.</p>
  <a class="abs btn hero-btn">Read More</a>

  <!-- Austin band -->
  <div class="abs austin">
    <svg width="856" height="266" viewBox="0 0 856 266" style="position:absolute;left:0;top:0">
      <defs><linearGradient id="bandGrad" x1="0" y1="0" x2="0" y2="1"><stop offset="0" stop-color="#b67a35"/><stop offset="1" stop-color="#8d4708"/></linearGradient></defs>
      <path d="M0 0H856V266C700 205 560 195 428 195C296 195 156 205 0 266Z" fill="url(#bandGrad)"/>
    </svg>
    <h2 class="abs display austin-title">We are based in Austin</h2>
    <p class="abs austin-sub">we work primarily with self-help, wellness, and diet authors</p>
    <span class="abs austin-badge"></span>
  </div>

  <!-- About -->
  <p class="abs eyebrow about-eyebrow">About</p>
  <h2 class="abs display section-title about-title">NRF Productions</h2>
  <p class="abs about-text">Nemo enim ipsam voluptatem quia voluptas sit aspernatur aut odit aut fugit, sed quia consequuntur magni dolores eos qui ratione voluptatem sequi nesciunt. Neque porro quisquam est, qui dolorem ipsum quia dolor sit amet, consectetur, adipisci velit, sed quia non numquam eius modi tempora incidunt ut labore et dolore magnam aliquam quaerat volupta tem. Ut enim ad minima veniam, quis nostrum exercitationem ullam cor poris suscipit laboriosam.</p>
  <a class="abs btn about-btn">Read More</a>
  <div class="abs about-photo" role="img" aria-label="Woman raising her arms toward a golden sunset over the sea"></div>
  <div class="abs about-ring"></div>
  <span class="abs about-badge"></span>

  <!-- We work with -->
  <svg class="abs work" viewBox="0 0 1200 713" role="img" aria-label="Two women sitting on a hilltop overlooking a valley, toned in amber">
    <defs><linearGradient id="workGrad" x1="0" y1="0" x2="0" y2="1"><stop offset="0" stop-color="#b86c1c"/><stop offset=".5" stop-color="#a9631d"/><stop offset="1" stop-color="#955010"/></linearGradient></defs>
    <path d="M0 0C120 60 230 74 380 70L1200 0V713C1130 660 1020 640 900 648L0 713Z" fill="url(#workGrad)"/>
  </svg>
  <p class="abs display work-eyebrow">We</p>
  <h2 class="abs display work-title">Work With</h2>

  <div class="abs service" style="left:147px;top:1619px">
    <div class="service-icon">
      <svg width="64" height="64" viewBox="0 0 64 64" fill="none" stroke="#222" stroke-width="2.5" stroke-linecap="round"><path d="M12 52C16 30 30 14 54 10C52 34 40 50 18 50Z"/><path d="M12 52C24 40 34 30 44 20"/></svg>
    </div>
    <h3>Wellness</h3>
    <p>Quis autem vel eum iure reprehenderit<br>qui in ea voluptate velit esse.</p>
  </div>
  <div class="abs service" style="left:450px;top:1619px">
    <div class="service-icon">
      <svg width="72" height="64" viewBox="0 0 72 64" fill="none" stroke="#222" stroke-width="2.5" stroke-linecap="round"><circle cx="46" cy="40" r="14"/><circle cx="20" cy="46" r="5"/><circle cx="28" cy="46" r="5"/><circle cx="24" cy="38" r="5"/><path d="M46 26C46 18 52 12 60 10C60 18 54 24 46 26Z"/><path d="M6 56H66"/></svg>
    </div>
    <h3>Diet Authors</h3>
    <p>Quis autem vel eum iure reprehenderit<br>qui in ea voluptate velit esse.</p>
  </div>
  <div class="abs service" style="left:750px;top:1619px">
    <div class="service-icon">
      <svg width="64" height="64" viewBox="0 0 64 64" fill="none" stroke="#222" stroke-width="2.5" stroke-linecap="round" stroke-linejoin="round"><path d="M14 34L26 14C28 11 32 13 30 16L26 24L38 20C41 19 42 23 39 24"/><path d="M20 46L14 34"/><path d="M26 28L40 28M26 34L40 34M24 40L36 40"/><path d="M46 10C56 20 56 40 44 54"/></svg>
    </div>
    <h3>Self-Help</h3>
    <p>Quis autem vel eum iure reprehenderit<br>qui in ea voluptate velit esse.</p>
  </div>

  <!-- Offer -->
  <p class="abs eyebrow offer-eyebrow">What</p>
  <h2 class="abs display section-title offer-title">NRF Offer</h2>

  <div class="abs card" style="left:172px">
    <div class="card-photo" role="img" aria-label="Dark fantasy artwork of skulls and a castle rising from an open book" style="background:linear-gradient(160deg,#3b4040,#151a1c 70%)"></div>
    <p class="card-label">Ghostwriting</p>
  </div>
  <div class="abs card" style="left:468px;background:#a4560e">
    <div class="card-photo" role="img" aria-label="Person lying in sunny grass reading a red book" style="background:linear-gradient(170deg,#f2eab0,#b8c05a 45%,#6d8a2e)"></div>
    <p class="card-label">Editing Service</p>
  </div>
  <div class="abs card" style="left:762px;background:var(--orange)">
    <div class="card-photo" role="img" aria-label="Stack of colourful books with an open book on top against a teal wall" style="background:linear-gradient(180deg,#4fb3bf,#6fc0c6 55%,#c9b886)"></div>
    <p class="card-label">Book Development</p>
  </div>

  <!-- Subscribe -->
  <svg class="abs subscribe" viewBox="0 0 1200 705" role="img" aria-label="Smiling woman with curly hair holding an open book in a library">
    <defs><linearGradient id="subGrad" x1="0" y1="0" x2="1" y2="0"><stop offset="0" stop-color="#3e3f46"/><stop offset=".55" stop-color="#6b6259"/><stop offset="1" stop-color="#8a7a66"/></linearGradient></defs>
    <path d="M0 0C40 60 90 80 150 80C500 70 900 40 1200 0V650C1120 620 1000 625 880 648L0 705Z" fill="url(#subGrad)"/>
  </svg>
  <p class="abs display sub-eyebrow">NRF</p>
  <h2 class="abs display sub-title">Subscribe With Us</h2>
  <p class="abs sub-text">Nemo enim ipsam voluptatem quia voluptas sit aspernatur aut odit aut fugit, sed quia consequuntur magni dolores.</p>
  <div class="abs email">Email</div>
  <a class="abs btn sub-btn">Subscribe</a>

  <!-- Footer -->
  <div class="abs brand footer-brand"><span class="brand-dot"></span><span class="brand-name">NRF Productions</span></div>
  <div class="abs col" style="left:472px;top:3488px">
    <h4>Quick Links</h4>
    <ul><li>Home</li><li>About</li><li>Blog</li><li>Events</li><li>Contact</li></ul>
  </div>
  <div class="abs col" style="left:615px;top:3488px">
    <h4>Links</h4>
    <ul><li>Quis Autem</li><li>Vel Eum Iure</li><li>Reprehenderit</li><li>Qui In Ea Voluptate</li><li>Velit Esse Quam</li></ul>
  </div>
  <div class="abs map" role="img" aria-label="Map of the Austin, Texas area"></div>
  <div class="abs rule"></div>
  <p class="abs copy">Copyrights @ 2021 NRF Productions. All Rights reserved.</p>

</div>
</body>
</html>
```